KORVELLA Corporate Business Card

Modern business card design for company which focuses in the areas of Staffing, IT Consulting & Data Services. Please note: We are no longer using the IT subscript on the logo. All designs should have IT subscript removed.
Website: www.korvellait.example

```html
<!DOCTYPE html>
<html lang="en">
<head>
<meta charset="utf-8">
<title>KORVELLA Business Card</title>
<link href="https://fonts.googleapis.com/css2?family=Open+Sans:wght@400;600;700&display=swap" rel="stylesheet">
<style>
  :root {
    --bg: #e6e6e6;
    --paper: #fbfbfb;
    --brand-blue: #1b68b2;
    --deep-blue: #0f4f94;
    --light-blue: #2f8fd6;
    --edge-blue: #3fa9e8;
    --ink: #4a4a4a;
    --white: #ffffff;
  }
  * { margin: 0; padding: 0; box-sizing: border-box; }
  html, body { width: 1200px; height: 801px; overflow: hidden; }
  body {
    background: var(--bg);
    font-family: "Open Sans", Arial, sans-serif;
    position: relative;
  }
  .card {
    position: absolute;
    top: 246px;
    width: 540px;
    height: 309px;
    box-shadow: 0 6px 18px rgba(0,0,0,0.18);
    border-bottom: 3px solid var(--edge-blue);
  }
  .card-front { left: 45px; background: var(--paper); }
  .card-back { left: 615px; background: var(--brand-blue); overflow: hidden; }

  .front-brand {
    position: absolute;
    left: 48px;
    top: 0;
    height: 100%;
    display: flex;
    align-items: center;
    gap: 8px;
  }
  .brand-square {
    width: 22px;
    height: 22px;
    background: var(--light-blue);
    border-radius: 3px;
  }
  .brand-name {
    font-weight: 600;
    font-size: 36px;
    letter-spacing: 1px;
    color: var(--light-blue);
  }
  .divider {
    position: absolute;
    left: 300px;
    top: 78px;
    width: 1px;
    height: 150px;
    background: var(--deep-blue);
  }
  .contact {
    position: absolute;
    left: 320px;
    top: 70px;
    color: var(--ink);
    font-size: 13px;
    line-height: 19px;
  }
  .person-name {
    font-weight: 700;
    font-size: 18px;
    color: var(--deep-blue);
    line-height: 22px;
  }
  .person-title { margin-bottom: 10px; }
  .address { margin-bottom: 10px; }
  .contact-row { display: flex; align-items: center; gap: 6px; }
  .contact-row svg { width: 11px; height: 11px; fill: var(--brand-blue); flex: none; }

  .back-pattern {
    position: absolute;
    inset: 0;
    background: linear-gradient(135deg, #1d6cb6 0%, #1862ab 100%);
  }
  .back-brand {
    position: absolute;
    right: 70px;
    top: 50%;
    transform: translateY(-50%);
    font-weight: 600;
    font-size: 26px;
    letter-spacing: 1px;
    color: var(--white);
  }
</style>
</head>
<body>
  <section class="card card-front">
    <div class="front-brand">
      <div class="brand-square"></div>
      <span class="brand-name">KORVELLA</span>
    </div>
    <div class="divider"></div>
    <div class="contact">
      <div class="person-name">DANA WHITLOCK</div>
      <div class="person-title">President</div>
      <div class="address">418 Larkfield Rd.<br>Brightwater, OH 44021</div>
      <div class="contact-row">
        <svg viewBox="0 0 12 12"><path d="M3 1l2 2.5-1.2 1.2a7 7 0 0 0 3.5 3.5L8.5 7 11 9l-1.3 2C5.5 11 1 6.5 1 2.3z"/></svg>
        <span>555-204-7719</span>
      </div>
      <div class="contact-row">
        <svg viewBox="0 0 12 12"><path d="M1 2.5h10v7H1z M1 2.5l5 4 5-4" stroke="#fff" stroke-width="0.8"/></svg>
        <span>hello@korvellait.example</span>
      </div>
      <div class="contact-row">
        <svg viewBox="0 0 12 12"><circle cx="6" cy="6" r="5"/></svg>
        <span>www.korvellait.example</span>
      </div>
    </div>
  </section>

  <section class="card card-back">
    <div class="back-pattern" role="img" aria-label="Repeating embossed pattern of the company symbol on blue"></div>
    <span class="back-brand">KORVELLA</span>
  </section>
</body>
</html>
```